Harbor Sushi & Steak Dinner Menu

I'm looking for a MENU design with a particular feel. I want to have a base template made that I can then use for future alterations to the menu; ie I can go in and change out different entrees as the menu changes but the template will remain the same. (Ideally it would be in an Apple Pages format.). Also ideally - dinner menu will occupy 2 pages 8.5 x 11. The restaurant's name is Harbor. It is a MODERN steak house that will also feature Sushi, a Raw Bar, Exquisite Cocktails and a sophisticated nightlife crowd. I have attached our LOGO, a secondary logo that we will be featuring throughout the project including on the menu cover (the gold U). Finally - I have attached the content that we would like to see. AGAIN - I REITERATE: High end dining and lounge atmosphere. A couple of restaurants / menus that I love are Corvellin in NYC and Marrowby Steakhouse in Long Island NY. Please do not duplicate - just trying to offer some suggestions.

Requirements
Must have
• A sophisticated and elegant feel without being stuffy or old.

```html
<!DOCTYPE html>
<html lang="en">
<head>
<meta charset="utf-8">
<title>Harbor Sushi &amp; Steak — Dinner Menu</title>
<link rel="stylesheet" href="https://fonts.googleapis.com/css2?family=Manrope:wght@400;700&display=swap">
<style>
  :root {
    --bg: #1c1a1f;
    --heading: #e9e7ec;
    --item: #1fa653;
    --sketch: #2e2c33;
    --ribbon-top: #c8c18c;
    --ribbon-bottom: #b27958;
    --ribbon-text: #1c1a1f;
  }
  * { margin: 0; padding: 0; box-sizing: border-box; }
  html, body { width: 927px; height: 1200px; overflow: hidden; background: var(--bg); }
  .menu-page {
    position: relative; width: 927px; height: 1200px; background: var(--bg);
    font-family: "Manrope", sans-serif; color: var(--item);
  }
  .section-title {
    position: absolute; left: 56px; font-size: 26px; font-weight: 700;
    color: var(--heading); letter-spacing: 0.2px; line-height: 1;
  }
  .item-list { position: absolute; left: 57px; list-style: none; font-size: 16px; line-height: 20.8px; letter-spacing: -0.1px; }
  .item-list.spaced li + li { margin-top: 8.5px; }
  .item-list .gap { margin-top: 20px; }
  .sketch { position: absolute; border-radius: 40px; background: var(--sketch); opacity: 0.55; }
  .brand-ribbon {
    position: absolute; left: 773px; top: 0; width: 75px; height: 129px;
  }
  .brand-ribbon .ribbon-name {
    position: absolute; left: 0; right: 0; top: 48px; text-align: center;
    font-size: 14px; font-weight: 700; color: var(--ribbon-text);
  }
</style>
</head>
<body>
<main class="menu-page">

  <div class="brand-ribbon">
    <svg width="75" height="129" viewBox="0 0 75 129" aria-hidden="true">
      <defs>
        <linearGradient id="ribbonFill" x1="0" y1="0" x2="0" y2="1">
          <stop offset="0" stop-color="var(--ribbon-top)"/>
          <stop offset="1" stop-color="var(--ribbon-bottom)"/>
        </linearGradient>
      </defs>
      <polygon points="0,0 75,0 75,129 37.5,120 0,129" fill="url(#ribbonFill)"/>
    </svg>
    <span class="ribbon-name">Harbor</span>
  </div>

  <div class="sketch" style="left:343px;top:44px;width:206px;height:69px;" role="img" aria-label="Line sketch of a corn dog"></div>
  <div class="sketch" style="left:694px;top:258px;width:182px;height:206px;" role="img" aria-label="Line sketch of french fries in a carton"></div>
  <div class="sketch" style="left:305px;top:950px;width:173px;height:173px;" role="img" aria-label="Line sketch of a pizza slice"></div>
  <div class="sketch" style="left:672px;top:1043px;width:193px;height:137px;" role="img" aria-label="Line sketch of a taco"></div>

  <h2 class="section-title" style="top:104px;">APPS</h2>
  <ul class="item-list" style="top:155px;">
    <li>BAO Bun; hoisin bbq pancetta cut pork loin,&nbsp; crispy onions, micro mint</li>
    <li>Five Spice Crispy Popcorn Crusted Prawns (2); classic burre blanc</li>
    <li>Jumbo Lump Crab; citrus miso drizzle, spring pea puree, micro greens</li>
    <li>Crispy Wonton Napoleon;&nbsp; cucumber gallete, ahi tuna, jumbo lump crab meat,<br>wasabi aioli, shoestring wontons</li>
    <li>PEI Mussels; charred artichoke hearts, blistered heirloom tomatoes, garlic white wine broth</li>
    <li>New Zealand or Domestic Small Eye Lamb Chop (1); crispy porcini risotto cake</li>
  </ul>

  <h2 class="section-title" style="top:323px;">SALADS</h2>
  <ul class="item-list spaced" style="top:364px;">
    <li>Classic Wedge; bleu cheese, bacon lardons, heirloom tomatoes</li>
    <li>Mixed Baby Greens; heirloom tomatoes, cucumber, red onion, dijon vinaigrette</li>
    <li>Tabulleh; buckwheat grain, fresh mint, tomato concasse, cucumber, parsley,<br>fresh squeezed lemon, EVOO., salt and pepper</li>
    <li>Tomato Mozzarella Salad / Burratta</li>
    <li>Spinach Salad; green apple, feta, currants, with per-simmons vinaigrette<br>Kale Caesar; homemade cacio e'peppe dressing, pecorino and parmesan cheese, toasted croutons.</li>
  </ul>

  <h2 class="section-title" style="top:576px;">ENTREES</h2>
  <ul class="item-list" style="top:619px;">
    <li>Pan Roasted Miso Glazed Black Cod; green tea noodle stir fry; Napa cabbage, carrot, Japanese eggplant</li>
    <li>Pan Seared Striped Bass; lobster succotash in a tomato saffron broth</li>
    <li>E.V.O.O. Salted / Grilled Swordfish; sun dried tomato, olive and caper tapenade, over basmati rice</li>
    <li>Grilled Half Chicken; sun dried tomato and basil Israeli cous-cous, pan au jus</li>
    <li>Roasted Fresh Caviatelle Ratatoille; vegetable broth</li>
    <li>Lobster Cartoccio; shrimp, mussels, clams, fresh herb tomato broth, tossed with bucatini</li>
    <li>Charred Artichoke Hearts, heirloom tomatoes, caper berries, spring onions, fresh basil,<br>white wine reduction over forbidden rice (gf)</li>
    <li class="gap">Mediterranean Grilled Veggie Plate; artichoke hearts, Japanese eggplant, green &amp; white asparagus,<br>seared heirloom tomatoes, roasted baby carrots, cauliflower rice, evoo &amp; fig drizzle (gf)</li>
  </ul>

  <h2 class="section-title" style="top:891px;">USDA PRIME STEAKS (gf)</h2>
  <ul class="item-list" style="top:941px;">
    <li>10 Oz Filet 14 or 16 oz</li>
    <li>New York Strip&nbsp; 24 oz</li>
    <li>Boneless Ribeye 36 oz</li>
    <li>Bone in Rib Eye</li>
    <li>Berkshire Pork Chop</li>
  </ul>

  <h2 class="section-title" style="top:897px;left:555px;">SAUCES</h2>
  <ul class="item-list" style="top:941px;left:555px;">
    <li>Cabernet Demi Glaz</li>
    <li>Gorganzola Brulle Cream</li>
    <li>Truffled Wild Mushroom Ragu</li>
    <li>Horseradish Cream</li>
    <li>House Steak Sauce</li>
  </ul>

  <h2 class="section-title" style="top:1076px;left:58px;">DESSERTS</h2>
  <ul class="item-list" style="top:1120px;left:58px;">
    <li>T.B.D. - separate menu</li>
  </ul>

</main>
</body>
</html>
```